Realty Group Needs Classy, Contemporary Letterhead Design

We need a letterhead design for a new realty company located in NY, USA. We buy investment properties to rehabilitate and or keep in our rental portfolio.

```html
<!DOCTYPE html>
<html lang="en">
<head>
<meta charset="utf-8">
<title>Meridian Realty Group Letterhead</title>
<link rel="stylesheet" href="https://fonts.googleapis.com/css2?family=Montserrat:wght@800&family=Mulish:wght@300&display=swap">
<style>
  :root {
    --brand-purple: #4f2a84;
    --ink-grey: #7b7b7b;
    --band-light: #f1f1f1;
    --band-grey: #7b7b7b;
    --paper: #ffffff;
  }
  html, body {
    margin: 0;
    padding: 0;
    overflow: hidden;
    background: var(--paper);
  }
  .letterhead {
    position: relative;
    width: 927px;
    height: 1200px;
    background: var(--paper);
    overflow: hidden;
  }
  .swoosh {
    position: absolute;
    inset: 0;
    width: 927px;
    height: 1200px;
  }
  .swoosh .band-light { fill: var(--band-light); }
  .swoosh .band-grey { fill: var(--band-grey); }
  .swoosh .band-purple { fill: var(--brand-purple); }

  .brand {
    position: absolute;
    top: 38px;
    left: 0;
    width: 927px;
    text-align: center;
    font-family: "Montserrat", sans-serif;
    font-weight: 800;
    color: var(--brand-purple);
  }
  .brand-name {
    display: block;
    font-size: 54px;
    line-height: 1;
    letter-spacing: 1px;
  }
  .brand-sub {
    display: block;
    margin-top: 8px;
    font-size: 17px;
    letter-spacing: 1.5px;
  }

  .contact {
    position: absolute;
    top: 144px;
    left: 270px;
    display: flex;
    gap: 10px;
    font-family: "Mulish", sans-serif;
    font-weight: 300;
    font-size: 15.5px;
    line-height: 18px;
    color: var(--ink-grey);
  }
  .contact-item {
    display: flex;
    align-items: flex-start;
    gap: 3px;
  }
  .contact-item svg {
    stroke: var(--ink-grey);
    fill: none;
    stroke-width: 0.8;
    flex-shrink: 0;
  }
  .contact-address { text-transform: uppercase; margin-left: 4px; }
</style>
</head>
<body>
  <div class="letterhead">
    <svg class="swoosh" viewBox="0 0 1688 2184" preserveAspectRatio="none" aria-hidden="true">
      <path class="band-light" d="M0,213 C500,450 1300,420 1688,195 L1688,290 C1300,440 700,470 0,262 Z"/>
      <path class="band-grey" d="M0,262 C500,470 1000,470 1180,425 C900,480 400,450 0,327 Z"/>
      <path class="band-purple" d="M240,315 C700,440 1300,390 1688,195 L1688,245 C1300,410 700,470 240,315 Z"/>
    </svg>

    <header class="brand">
      <span class="brand-name">MERIDIAN</span>
      <span class="brand-sub">Realty Group, LLC</span>
    </header>

    <div class="contact">
      <div class="contact-item contact-phone">
        <svg width="13" height="22" viewBox="0 0 13 22">
          <rect x="0.5" y="0.5" width="12" height="21" rx="1.5"/>
          <rect x="1.8" y="3" width="9.4" height="13"/>
          <rect x="5" y="18" width="3" height="1.5"/>
          <line x1="4.5" y1="1.7" x2="8.5" y2="1.7"/>
        </svg>
        <div>555 014 2870<br>555 016 4419</div>
      </div>
      <div class="contact-item">
        <svg width="14" height="20" viewBox="0 0 14 20">
          <path d="M7,19 L1.5,9.5 A6,6 0 1 1 12.5,9.5 Z"/>
          <circle cx="7" cy="6.5" r="2.4"/>
        </svg>
        <div class="contact-address">1480 Harbor View Ave # 4<br>Lakeport, NY 12345</div>
      </div>
    </div>
  </div>
</body>
</html>
```